Dental Practice Billboard Design

We are a newer dental practice in need of a simple but appealing billboard for our growing dental practice to attract new patients. The practice is owned by husband and wife dentists and is family friendly in a small town in Kentucky. We try to be very friendly and caring to our patients. Would prefer a blue background for the billboard and our tooth logo to be prominent. We are partial to the Patua One font used in the image below but please feel free to tweak it as you deem necessary. The shape of the uppercase D and lowercase g are why we like that font, so fonts with a similarly shaped “D” and “g” would work as well. Please include our phone number (606) 847-3962. Please see our website Harlowfamilydentistry.com for more info on the practice if needed. Thank you! Looking forward to seeing your creation.
Updates

The dimensions will be 12ft x 24ft (3.6576m x 7.3152m). Apologies for not including this in the original prompt. Thank you all for your submissions.

Industry/Entity Type

Dental

Font styles to use
Other font styles liked:
• Patua One

Colors
0054AA
0677BA
7BADD7
CADEEF
E8F1F8
0094D4
00A9DD
6FCCEA
C7EBF8
E9F6FB
00AB8E
00BBA5
67D7C9
C6EFE9
E9F9F6
59FF00
82FF00
B8FF75
E3FFCB
F4FFEA

Requirements
Must have
• Phone number, website, Logo, Practice name “Harlow Family Dentistry”
Should not have
• A tagline or slogan

```html
<!DOCTYPE html>
<html lang="en">
<head>
<meta charset="utf-8">
<title>Harlow Family Dentistry – Billboard</title>
<link href="https://fonts.googleapis.com/css2?family=Patua+One&display=swap" rel="stylesheet">
<style>
  :root {
    --page: #eef1f5;
    --board-blue: #27408b;
    --white: #ffffff;
    --green: #6cb33f;
    --teal: #4fb5aa;
  }
  * { margin: 0; padding: 0; box-sizing: border-box; }
  html, body {
    width: 1200px;
    height: 1000px;
    overflow: hidden;
    background: var(--page);
    font-family: "Patua One", Georgia, serif;
  }
  .billboard {
    position: absolute;
    left: 0;
    top: 200px;
    width: 1200px;
    height: 600px;
    background: var(--board-blue);
    color: var(--white);
  }
  .brand-mark {
    position: absolute;
    left: 68px;
    top: 82px;
    width: 300px;
    height: 300px;
    border-radius: 50%;
    background: var(--white);
  }
  .practice-name,
  .practice-type {
    position: absolute;
    left: 415px;
    line-height: 1;
    white-space: nowrap;
    color: var(--white);
    font-weight: 400;
  }
  .practice-name { top: 42px; font-size: 176px; letter-spacing: -1px; }
  .practice-type { top: 242px; font-size: 78px; }
  .contact-line {
    position: absolute;
    left: 0;
    width: 100%;
    top: 445px;
    text-align: center;
    font-size: 23px;
    line-height: 1;
  }
  .divider {
    position: absolute;
    left: 0;
    top: 484px;
    width: 100%;
    height: 3px;
    background: var(--green);
  }
  .call-to-action {
    position: absolute;
    left: 0;
    width: 100%;
    top: 498px;
    text-align: center;
    font-size: 84px;
    line-height: 1;
    white-space: nowrap;
  }
  .call-to-action .prompt { color: var(--teal); letter-spacing: 1px; }
  .call-to-action .phone { color: var(--white); }
</style>
</head>
<body>
  <main class="billboard">
    <div class="brand-mark" aria-hidden="true"></div>
    <h1>
      <span class="practice-name">Harlow</span>
      <span class="practice-type">Family Dentistry</span>
    </h1>
    <p class="contact-line">Harlowfamilydentistry@gmail.com | Harlowfamilydentistry.com</p>
    <div class="divider"></div>
    <p class="call-to-action"><span class="prompt">CALL TODAY!</span> <span class="phone">(606) 847-3962</span></p>
  </main>
</body>
</html>
```